Lumo Ket

Need business cards designed. Project is an Lumo Ket in Hollywood. It'll include 3 live theatre, a restaurant and event space.

Target Market(s)

Across the board, young and old.

Industry/Entity Type

Entertainment

Contact Information for Business Card

Be creative. This is a creative venture that I'm building.

```html
<!DOCTYPE html>
<html lang="en">
<head>
<meta charset="utf-8">
<title>Lumo Ket – Business Cards</title>
<link rel="stylesheet" href="https://fonts.googleapis.com/css2?family=Poppins:wght@600&family=Didact+Gothic&display=swap">
<style>
  :root{
    --backdrop:#1b1b1b;
    --card-dark:#2f2f2f;
    --card-shade:#474747;
    --card-light:#ffffff;
    --gold:#e4b050;
    --gold-deep:#eaa923;
    --gold-end:#d39b2a;
    --ink:#3a3a3a;
    --disc:#3c3c3c;
  }
  *{margin:0;padding:0;box-sizing:border-box}
  html,body{width:1200px;height:998px;overflow:hidden;background:var(--backdrop)}
  .canvas{position:relative;width:1200px;height:998px}
  .card{position:absolute;overflow:hidden}
  .card svg.shapes{position:absolute;left:0;top:0;width:100%;height:100%}

  /* front */
  .card-front{left:277px;top:97px;width:606px;height:363px;background:var(--card-dark)}
  .brand-name{position:absolute;left:0;width:100%;top:162px;text-align:center;
    font-family:'Poppins',sans-serif;font-weight:600;font-size:25px;line-height:32px;color:var(--gold)}
  .brand-tagline{position:absolute;left:0;width:100%;top:196px;text-align:center;
    font-family:'Didact Gothic',sans-serif;font-size:10.5px;letter-spacing:1.4px;color:var(--gold)}

  /* back */
  .card-back{left:277px;top:528px;width:622px;height:364px;background:var(--card-dark)}
  .contact-list{position:absolute;left:72px;top:0;list-style:none;
    font-family:'Didact Gothic',sans-serif;font-size:13px;letter-spacing:1.3px;color:var(--ink)}
  .contact-list li{position:absolute;left:0;white-space:nowrap;line-height:16px}
  .contact-phone{top:118px}
  .contact-email{top:178px}
  .contact-address{top:241px}
  .holder-name{position:absolute;left:302px;width:320px;top:145px;text-align:center;
    font-family:'Didact Gothic',sans-serif;font-size:27px;letter-spacing:1.5px;color:var(--gold)}
  .holder-role{position:absolute;left:302px;width:320px;top:189px;text-align:center;
    font-family:'Didact Gothic',sans-serif;font-size:10.5px;letter-spacing:2.8px;color:var(--gold)}
</style>
</head>
<body>
<main class="canvas">

  <section class="card card-front" aria-label="Card front">
    <svg class="shapes" viewBox="0 0 758 454" preserveAspectRatio="none" aria-hidden="true">
      <defs>
        <linearGradient id="band-gold" x1="0" x2="1" y1="0" y2="0">
          <stop offset="0" stop-color="var(--gold-deep)"/>
          <stop offset="1" stop-color="var(--gold-end)"/>
        </linearGradient>
      </defs>
      <path class="top-tab" d="M132 0 H626 L572 38 Q556 51 530 51 H228 Q202 51 186 38 Z" fill="var(--card-shade)"/>
      <circle class="brand-dot" cx="379" cy="149" r="28" fill="var(--gold)"/>
      <line x1="0" y1="227" x2="276" y2="227" stroke="var(--gold)" stroke-width="2"/>
      <line x1="483" y1="227" x2="758" y2="227" stroke="var(--gold)" stroke-width="2"/>
      <rect class="bottom-band" x="0" y="417" width="758" height="37" fill="url(#band-gold)"/>
      <path class="bottom-tab" d="M132 454 L186 416 Q202 403 228 403 H530 Q556 403 572 416 L626 454 Z" fill="var(--gold)"/>
    </svg>
    <h1 class="brand-name">Lumo Ket</h1>
    <p class="brand-tagline">Theatre, Restaurant and Event space</p>
  </section>

  <section class="card card-back" aria-label="Card back">
    <svg class="shapes" viewBox="0 0 778 455" preserveAspectRatio="none" aria-hidden="true">
      <path class="light-panel" d="M0 0 H378 L350 46 Q341 62 341 85 V370 Q341 393 350 409 L378 455 H0 L36 401 Q46 386 46 370 V85 Q46 69 36 54 Z" fill="var(--card-light)"/>
      <path class="gold-strip" d="M378 0 L350 46 Q341 62 341 85 V370 Q341 393 350 409 L378 455 Z" fill="var(--gold)"/>
      <!-- icon tabs -->
      <rect x="24" y="137" width="42" height="42" rx="9" fill="var(--card-dark)"/>
      <rect x="24" y="212" width="42" height="42" rx="9" fill="var(--card-dark)"/>
      <rect x="24" y="291" width="42" height="42" rx="9" fill="var(--card-dark)"/>
      <!-- phone -->
      <path d="M35 148 q3 -2 5 0 l3 5 q1 2 -1 4 l-2 1 q2 5 7 8 l1 -2 q2 -2 4 -1 l5 3 q2 2 0 5 l-2 2 q-4 3 -11 -2 q-8 -6 -11 -14 q-1 -5 2 -9 z" fill="var(--gold)"/>
      <!-- globe -->
      <g fill="none" stroke="var(--gold)" stroke-width="2">
        <circle cx="45" cy="233" r="14"/>
        <ellipse cx="45" cy="233" rx="6" ry="14"/>
        <line x1="31" y1="233" x2="59" y2="233"/>
        <line x1="33" y1="226" x2="57" y2="226"/>
        <line x1="33" y1="240" x2="57" y2="240"/>
        <line x1="45" y1="219" x2="45" y2="247"/>
      </g>
      <!-- pin -->
      <path d="M45 298 a10 10 0 0 1 10 10 c0 7 -10 18 -10 18 s-10 -11 -10 -18 a10 10 0 0 1 10 -10 z" fill="var(--gold)"/>
      <circle cx="45" cy="308" r="3.5" fill="var(--card-dark)"/>
      <!-- faint backdrop disc -->
      <circle cx="577" cy="268" r="72" fill="var(--disc)"/>
      <circle cx="577" cy="268" r="44" fill="var(--card-dark)" opacity="0.5"/>
    </svg>
    <ul class="contact-list">
      <li class="contact-phone">323.555.0142</li>
      <li class="contact-email">dmerrow@mail.com</li>
      <li class="contact-address">412 N.Larkspur Ave</li>
    </ul>
    <h2 class="holder-name">Dana Merrow</h2>
    <p class="holder-role">CREATIVE DIRECTOR</p>
  </section>

</main>
</body>
</html>
```